Bidmark Display ads for Real Estate Photography

I'm looking for someone to take ideas off of my flyers and website (lensvale.example) to create two sets of display ads. One for branding and another for specific specials (see magazine-ad-special.pdf). I would like these to be animated gifs that cycle between 2 or 3 views. Here are the dimensions for the ads:
300 x 250 – Inline Rectangle
728 x 90 – Leaderboard
160 x 600 – Wide Skyscraper
320×100 - Large Mobile Banner
I can also provide source artwork from the flyers if needed.
Target Market(s)
Realtors that sell high end luxury homes
Industry/Entity Type
Professional Photography
Requirements
Must have
- .psd source files for each size ad with screens/views on different layers to I can export as an animated gif
- display ads in the following sizes:
- 300 x 250 – Inline Rectangle
- 728 x 90 – Leaderboard
- 160 x 600 – Wide Skyscraper
- 320×100 - Large Mobile Banner
Nice to have
- 336 x 280 – Large Rectangle
- 300 x 600 – Half-Page Ad

```html
<!DOCTYPE html>
<html lang="en">
<head>
<meta charset="utf-8">
<title>Lensvale Display Ads – Scenes</title>
<link rel="stylesheet" href="https://fonts.googleapis.com/css2?family=Open+Sans:wght@600;700&family=Questrial&display=swap">
<style>
:root{
  --paper:#ecedee;
  --navy:#1f2a55;
  --board:#1e2227;
  --board-light:#353b44;
  --brand-blue:#1f6fc0;
  --bar:#2b2b2b;
  --accent-blue:#3b9bf0;
  --accent-orange:#f3a233;
  --label-yellow:#f2c200;
  --white:#ffffff;
}
*{margin:0;padding:0;box-sizing:border-box}
html,body{width:1200px;height:1200px;overflow:hidden}
body{position:relative;background:radial-gradient(ellipse at 50% 25%,var(--board-light),var(--board) 70%);font-family:"Questrial",sans-serif}
.board-header{position:absolute;left:0;top:0;width:1200px;height:126px;background:var(--paper);border-bottom:2px solid #111;text-align:center;padding-top:50px}
.board-header p{font-family:"Open Sans",sans-serif;font-weight:700;color:var(--navy);font-size:22px;letter-spacing:5px;line-height:29px}
.ad{position:absolute;width:530px;height:440px;border:2px solid #e6e6e6;overflow:hidden;background:var(--bar)}
.ad--brand{left:80px;top:198px}
.ad--imagery{left:661px;top:198px}
.ad--contact{left:346px;top:666px}
.ad__photo{position:absolute;left:0;top:0;width:100%;height:348px}
.ad__photo--kitchen{background:linear-gradient(160deg,#f4f4f2 0%,#d9d3c8 40%,#a88b6a 70%,#6b5440 100%)}
.ad__photo--bedroom{background:linear-gradient(170deg,#f6f6f4 0%,#e4e1da 45%,#c9b69b 75%,#8d7a62 100%)}
.ad__header{position:absolute;left:0;top:0;width:530px;height:140px}
.ad__name{position:absolute;left:16px;top:28px;font-size:40px;color:var(--white);letter-spacing:1px}
.ad__bar{position:absolute;left:0;top:348px;width:100%;height:92px;background:var(--bar);text-align:center}
.ad__line{display:block;line-height:1}
.ad__line--white{color:var(--white);font-size:31px;padding-top:12px;letter-spacing:1px}
.ad__line--blue{color:var(--accent-blue);font-size:41px;padding-top:6px}
.ad__line--orange{color:var(--accent-orange);font-size:33px;padding-top:12px;letter-spacing:1px}
.ad__line--sub{color:var(--white);font-size:23px;padding-top:8px}
.contact{position:absolute;top:12px;text-align:center}
.contact--call{left:12px;width:240px}
.contact--visit{right:12px;width:240px}
.contact__label{display:block;color:var(--accent-orange);font-size:26px}
.contact__value{display:block;color:var(--white);font-size:31px;padding-top:10px}
.scene-label{position:absolute;font-family:"Open Sans",sans-serif;font-weight:700;color:var(--label-yellow);font-size:23px;letter-spacing:5px}
.scene-label--1{left:157px;top:674px}
.scene-label--2{left:945px;top:657px}
.scene-label--3{left:553px;top:1128px}
</style>
</head>
<body>
<header class="board-header">
  <p>EDITABLE COVER PAGEDESIGN</p>
  <p>OLD AND NEW COMPARE</p>
</header>

<section class="ad ad--brand">
  <div class="ad__photo ad__photo--kitchen" role="img" aria-label="Bright luxury kitchen with pendant lamps, stone wall and wooden island"></div>
  <svg class="ad__header" viewBox="0 0 530 140"><path d="M0 0H530V32Q290 44 0 138Z" fill="var(--brand-blue)"/><path d="M0 138Q290 44 530 32" fill="none" stroke="#fff" stroke-width="3"/></svg>
  <span class="ad__name">Lensvale</span>
  <div class="ad__bar">
    <span class="ad__line ad__line--white">GROW YOUR BUSINESS</span>
    <span class="ad__line ad__line--blue">&amp; SELL MORE HOMES</span>
  </div>
</section>

<section class="ad ad--imagery">
  <div class="ad__photo ad__photo--bedroom" role="img" aria-label="Airy white bedroom with vaulted beams, armchairs and blue striped pillows"></div>
  <svg class="ad__header" viewBox="0 0 530 140"><path d="M0 0H530V32Q290 44 0 138Z" fill="var(--brand-blue)"/><path d="M0 138Q290 44 530 32" fill="none" stroke="#fff" stroke-width="3"/></svg>
  <span class="ad__name">Lensvale</span>
  <div class="ad__bar">
    <span class="ad__line ad__line--orange">BEAUTIFUL VIVID IMEGERY</span>
    <span class="ad__line ad__line--sub">that will set your listings apart from the rest!</span>
  </div>
</section>

<section class="ad ad--contact">
  <div class="ad__photo ad__photo--bedroom" role="img" aria-label="Airy white bedroom with vaulted beams, armchairs and blue striped pillows"></div>
  <svg class="ad__header" viewBox="0 0 530 140"><path d="M0 0H530V32Q290 44 0 138Z" fill="var(--brand-blue)"/><path d="M0 138Q290 44 530 32" fill="none" stroke="#fff" stroke-width="3"/></svg>
  <span class="ad__name">Lensvale</span>
  <div class="ad__bar">
    <div class="contact contact--call"><span class="contact__label">CALL US:</span><span class="contact__value">555.014.0199</span></div>
    <div class="contact contact--visit"><span class="contact__label">VISIT US:</span><span class="contact__value">lensvale.example</span></div>
  </div>
</section>

<span class="scene-label scene-label--1">SCENE 1</span>
<span class="scene-label scene-label--2">SCENE 2</span>
<span class="scene-label scene-label--3">SCENE 3</span>
</body>
</html>
```